Business Card Design Project for MirellaVontane

Our company needs a Business Card Design. Please refer to our original project in the link above.

Business Card will have the Logo&Symbol withe the Corporate Identity that is beeing created in PixelForum. Pls see other MirellaVontane Projects.

Target Market(s)

Luxury fashion interested women

Industry/Entity Type

Business

Font styles to use
Other font styles liked:
• Calibri, Arial, Myriad, Helvetica Neue, Lucida Grande, Avenir

```html
<!DOCTYPE html>
<html lang="en">
<head>
<meta charset="utf-8">
<title>MirellaVontane Business Card</title>
<link rel="stylesheet" href="https://fonts.googleapis.com/css2?family=Marcellus&family=Lato:wght@400&display=swap">
<style>
  :root {
    --navy: #22266d;
    --gold: #c9a227;
    --paper: #ffffff;
    --ink: #2b2b2b;
    --backdrop: #4d4d4d;
  }
  * { margin: 0; padding: 0; box-sizing: border-box; }
  html, body { width: 1200px; height: 750px; overflow: hidden; }
  body { background: var(--backdrop); position: relative; font-family: "Lato", Arial, sans-serif; }

  .card { position: absolute; box-shadow: 0 6px 14px rgba(0,0,0,0.45); }

  .card-front {
    left: 632px; top: 70px; width: 510px; height: 306px;
    background: var(--paper);
    border-top: 5px solid var(--navy);
    border-bottom: 5px solid var(--gold);
  }
  .brand-name {
    position: absolute; left: 0; right: 0; top: 52px;
    text-align: center;
    font-family: "Marcellus", Georgia, serif;
    font-size: 28px; letter-spacing: 6px;
    color: var(--navy);
  }
  .person { position: absolute; left: 0; right: 0; top: 152px; text-align: center; }
  .person-name {
    font-family: "Marcellus", Georgia, serif;
    font-size: 19px; letter-spacing: 2.5px; color: var(--ink);
  }
  .person-role { font-size: 10.5px; color: var(--navy); margin-top: 2px; }

  .contact { position: absolute; top: 216px; list-style: none; font-size: 12.5px; color: var(--ink); }
  .contact li { display: flex; align-items: center; height: 18.5px; gap: 10px; }
  .contact svg { width: 12px; height: 12px; flex: none; }
  .contact-left { left: 30px; }
  .contact-right { right: 30px; text-align: right; }
  .contact-right li { justify-content: flex-end; }

  .card-back {
    left: 59px; top: 377px; width: 542px; height: 298px;
    background: var(--navy);
    display: flex; align-items: center; justify-content: center;
  }
  .back-brand {
    font-family: "Marcellus", Georgia, serif;
    font-size: 28px; letter-spacing: 6px; color: var(--paper);
  }
</style>
</head>
<body>

<section class="card card-front" aria-label="Business card front">
  <div class="brand-name">MIRELLA VONTANE</div>

  <div class="person">
    <div class="person-name">JULIAN MAREK</div>
    <div class="person-role">Managing Director</div>
  </div>

  <ul class="contact contact-left">
    <li>
      <svg viewBox="0 0 12 12" aria-hidden="true"><rect x="3" y="1" width="6" height="10" rx="1" fill="none" stroke="var(--gold)" stroke-width="1.2"/><circle cx="6" cy="9.2" r="0.6" fill="var(--gold)"/></svg>
      <span>+63 7 2100 5630</span>
    </li>
    <li>
      <svg viewBox="0 0 12 12" aria-hidden="true"><path d="M1 4.5 Q6 1 11 4.5 L10 6 L8 5 L8 4 Q6 3.4 4 4 L4 5 L2 6 Z" fill="var(--gold)"/><rect x="2.5" y="6.5" width="7" height="4" rx="0.8" fill="var(--gold)"/></svg>
      <span>+63 7 2100 5630</span>
    </li>
    <li>
      <svg viewBox="0 0 12 12" aria-hidden="true"><rect x="1" y="2.5" width="10" height="7" fill="none" stroke="var(--gold)" stroke-width="1.1"/><path d="M1 2.5 L6 6.5 L11 2.5" fill="none" stroke="var(--gold)" stroke-width="1.1"/></svg>
      <span>julian@yoursite.com</span>
    </li>
  </ul>

  <ul class="contact contact-right">
    <li>
      <span>123 Name Street</span>
      <svg viewBox="0 0 12 12" aria-hidden="true"><path d="M6 11.5 C3 7.5 2 6 2 4.5 A4 4 0 0 1 10 4.5 C10 6 9 7.5 6 11.5 Z" fill="var(--gold)"/><circle cx="6" cy="4.5" r="1.5" fill="var(--paper)"/></svg>
    </li>
    <li>
      <span>Name City, 12345 Name State</span>
      <svg viewBox="0 0 12 12" aria-hidden="true"></svg>
    </li>
    <li>
      <span>www.yoursite.com</span>
      <svg viewBox="0 0 12 12" aria-hidden="true"><circle cx="6" cy="6" r="4.8" fill="none" stroke="var(--gold)" stroke-width="1.1"/><ellipse cx="6" cy="6" rx="2" ry="4.8" fill="none" stroke="var(--gold)" stroke-width="0.9"/><line x1="1.2" y1="6" x2="10.8" y2="6" stroke="var(--gold)" stroke-width="0.9"/></svg>
    </li>
  </ul>
</section>

<section class="card card-back" aria-label="Business card back">
  <div class="back-brand">MIRELLA VONTANE</div>
</section>

</body>
</html>
```